Modern Label for cleaning products for the brand Voralux

We need a label design for our line of cleaning products. The label should feature our logo and an image to identify the product's intended use. I've added our logo and an image for use. This only concerns the design of the label on the front of the bottle.

Label dimensions:
Label 1 (500ml bottle with spray): width 58mm x height 115mm
Label 2: (1L bottle): width 73mm x height 140mm
The design must be consistent for both bottles which you find in the pictures.

The bottles to be labeled are white. See the attachment for a photo of the bottles.

The photo must also appear on the label to identify the product's intended use.

Product information:
Brand: Voralux
Product: Sanitary Cleaner

This text must be placed on the label:
"Cleans, descales & freshens. followed with this text: "Ideal for quick and powerful cleaning. A ready-to-use product for everyday use."

- Mention the seperate USP's: Sanitary, Bathroom, Toilet, Wet areas

Appearance: This is a consumer product, but it must have a professional appearance. We would like to see a design that use the color blue from our logo.

Target Market(s)

Consumers who take care of their homes and want to maintain it the correct (professional) way

Font styles to use
Sans Serif

Colors
0054AA
0677BA
7BADD7
CADEEF
E8F1F8

Requirements
Must have
• USP's + use of image and logo + blend in 1 design
Nice to have
• Keep the color of the logo in the design
Should not have
• Comic sans

```html
<!DOCTYPE html>
<html lang="en">
<head>
<meta charset="utf-8">
<title>Voralux Sanitary Cleaner – Front Labels</title>
<link rel="stylesheet" href="https://fonts.googleapis.com/css2?family=Montserrat:ital,wght@1,800;1,900&family=Poppins:ital,wght@0,400;0,500;0,700;1,700&display=swap">
<style>
  :root{
    --brand-blue:#0054AA;
    --mid-blue:#0677BA;
    --deep-blue:#0a4a9e;
    --sky-blue:#00A8EE;
    --soft-blue:#7BADD7;
    --pale-blue:#CADEEF;
    --mist:#E8F1F8;
    --ink:#1b1b1b;
    --white:#ffffff;
    --page:#ffffff;
  }
  *{margin:0;padding:0;box-sizing:border-box}
  html,body{width:1200px;height:989px;overflow:hidden;background:var(--page)}
  .canvas{position:relative;width:1200px;height:989px}
  .label{position:absolute;container-type:inline-size;filter:drop-shadow(0 0 1px rgba(0,0,0,.08))}
  .label--500{left:167px;top:151px;width:342px;height:678px}
  .label--1000{left:593px;top:77px;width:430px;height:825px}
  .label__shape{position:absolute;inset:0;width:100%;height:100%}
  .label__layer{position:absolute;left:0;width:100%;text-align:center}

  .brand{top:3.2%}
  .brand__dot{display:block;margin:0 auto;width:21cqw;height:21cqw;border-radius:50%;background:var(--brand-blue)}
  .brand__name{display:block;margin-top:1.5cqw;font-family:"Poppins",sans-serif;font-weight:700;font-size:12cqw;line-height:1;color:var(--ink);letter-spacing:-.01em}

  .title{top:29%;font-family:"Montserrat",sans-serif;font-style:italic;font-weight:900;line-height:.92;letter-spacing:-.03em}
  .title__line{display:block;font-size:14.5cqw;
    text-shadow:0 0 0 #fff,1.2cqw 0 0 #fff,-1.2cqw 0 0 #fff,0 1.2cqw 0 #fff,0 -1.2cqw 0 #fff,.85cqw .85cqw 0 #fff,-.85cqw .85cqw 0 #fff,.85cqw -.85cqw 0 #fff,-.85cqw -.85cqw 0 #fff,1.6cqw 1.6cqw 2cqw rgba(0,20,60,.35)}
  .title__line--top{color:var(--deep-blue);transform:translateX(1.5cqw)}
  .title__line--bottom{color:var(--sky-blue);transform:translateX(0)}

  .claim{top:46.3%;font-family:"Poppins",sans-serif;color:var(--white)}
  .claim__main{display:block;font-weight:700;font-style:italic;font-size:4.9cqw;line-height:1.3}
  .claim__sub{display:block;font-weight:700;font-size:3.55cqw;margin-top:1.2cqw}

  .usps{top:89.6%;display:flex;justify-content:center;gap:2.6cqw;font-family:"Poppins",sans-serif;font-weight:400;font-size:4.3cqw;color:var(--mid-blue)}
  .usp{display:inline-flex;align-items:center;gap:.4cqw;white-space:nowrap}
  .usp__tick{width:3.8cqw;height:3.8cqw}

  .footer{bottom:0;height:4.6%;display:flex;align-items:center;font-family:"Poppins",sans-serif;color:var(--white)}
  .footer__note{width:79%;font-weight:500;font-size:3.5cqw;letter-spacing:.17em;line-height:1.05}
  .footer__volume{width:21%;font-weight:500;font-size:4.2cqw}
</style>
</head>
<body>
<main class="canvas">

  <!-- 500 ml label -->
  <section class="label label--500">
    <svg class="label__shape" viewBox="0 0 600 1200" preserveAspectRatio="none" aria-hidden="false">
      <defs>
        <clipPath id="outline-a"><path d="M0,90 Q0,30 60,22 Q300,-12 540,22 Q600,30 600,90 V1152 Q600,1200 552,1200 H48 Q0,1200 0,1152 Z"/></clipPath>
        <radialGradient id="band-a" cx="50%" cy="40%" r="70%">
          <stop offset="0" stop-color="#2a8fe0"/><stop offset=".55" stop-color="#0d5db8"/><stop offset="1" stop-color="#07479a"/>
        </radialGradient>
        <linearGradient id="silver-a" x1="0" x2="1">
          <stop offset="0" stop-color="#6d6f78"/><stop offset=".5" stop-color="#eef0f4"/><stop offset="1" stop-color="#6d6f78"/>
        </linearGradient>
        <linearGradient id="room-a" x1="0" x2="1">
          <stop offset="0" stop-color="#8e8c8a"/><stop offset=".45" stop-color="#d8d8d6"/><stop offset=".7" stop-color="#f1f1f0"/><stop offset="1" stop-color="#9a9996"/>
        </linearGradient>
      </defs>
      <g clip-path="url(#outline-a)">
        <rect width="600" height="1200" fill="var(--white)"/>
        <g role="img" aria-label="Photo of a modern bathroom with walk-in shower, washbasin, bathtub and towel radiator">
          <rect y="600" width="600" height="560" fill="url(#room-a)"/>
        </g>
        <path d="M0,222 Q300,300 600,222 L600,252 Q300,332 0,252 Z" fill="url(#silver-a)"/>
        <path d="M0,250 Q300,330 600,250 L600,700 Q300,600 0,700 Z" fill="url(#band-a)"/>
        <path d="M0,700 Q300,600 600,700 L600,732 Q300,640 0,732 Z" fill="url(#silver-a)"/>
        <rect y="1146" width="475" height="54" fill="var(--brand-blue)"/>
        <rect x="475" y="1146" width="125" height="54" fill="var(--sky-blue)"/>
      </g>
    </svg>
    <div class="label__layer brand"><span class="brand__dot"></span><span class="brand__name">Voralux</span></div>
    <h1 class="label__layer title"><span class="title__line title__line--top">SANITARY</span><span class="title__line title__line--bottom">CLEANER</span></h1>
    <p class="label__layer claim"><span class="claim__main">CLEANS, DESCALES &amp; FRESHENS</span><span class="claim__sub">IDEAL FOR QUICK AND POWERFUL CLEANING</span></p>
    <ul class="label__layer usps">
      <li class="usp"><svg class="usp__tick" viewBox="0 0 20 20"><circle cx="10" cy="10" r="8.5" fill="none" stroke="var(--sky-blue)" stroke-width="1.6"/><path d="M6 10.5l3 3 5-7" fill="none" stroke="var(--sky-blue)" stroke-width="1.8"/></svg>Sanitary</li>
      <li class="usp"><svg class="usp__tick" viewBox="0 0 20 20"><circle cx="10" cy="10" r="8.5" fill="none" stroke="var(--sky-blue)" stroke-width="1.6"/><path d="M6 10.5l3 3 5-7" fill="none" stroke="var(--sky-blue)" stroke-width="1.8"/></svg>Bathroom</li>
      <li class="usp"><svg class="usp__tick" viewBox="0 0 20 20"><circle cx="10" cy="10" r="8.5" fill="none" stroke="var(--sky-blue)" stroke-width="1.6"/><path d="M6 10.5l3 3 5-7" fill="none" stroke="var(--sky-blue)" stroke-width="1.8"/></svg>Toilet</li>
      <li class="usp"><svg class="usp__tick" viewBox="0 0 20 20"><circle cx="10" cy="10" r="8.5" fill="none" stroke="var(--sky-blue)" stroke-width="1.6"/><path d="M6 10.5l3 3 5-7" fill="none" stroke="var(--sky-blue)" stroke-width="1.8"/></svg>Wet areas</li>
    </ul>
    <div class="label__layer footer"><span class="footer__note">A READY-TO-USE PRODUCT<br>FOR EVERYDAY USE</span><span class="footer__volume">500ml</span></div>
  </section>

  <!-- 1000 ml label -->
  <section class="label label--1000">
    <svg class="label__shape" viewBox="0 0 600 1200" preserveAspectRatio="none">
      <defs>
        <clipPath id="outline-b"><path d="M0,90 Q0,30 60,22 Q300,-12 540,22 Q600,30 600,90 V1152 Q600,1200 552,1200 H48 Q0,1200 0,1152 Z"/></clipPath>
        <radialGradient id="band-b" cx="50%" cy="40%" r="70%">
          <stop offset="0" stop-color="#2a8fe0"/><stop offset=".55" stop-color="#0d5db8"/><stop offset="1" stop-color="#07479a"/>
        </radialGradient>
        <linearGradient id="silver-b" x1="0" x2="1">
          <stop offset="0" stop-color="#6d6f78"/><stop offset=".5" stop-color="#eef0f4"/><stop offset="1" stop-color="#6d6f78"/>
        </linearGradient>
        <linearGradient id="room-b" x1="0" x2="1">
          <stop offset="0" stop-color="#8e8c8a"/><stop offset=".45" stop-color="#d8d8d6"/><stop offset=".7" stop-color="#f1f1f0"/><stop offset="1" stop-color="#9a9996"/>
        </linearGradient>
      </defs>
      <g clip-path="url(#outline-b)">
        <rect width="600" height="1200" fill="var(--white)"/>
        <g role="img" aria-label="Photo of a modern bathroom with walk-in shower, washbasin, bathtub and towel radiator">
          <rect y="600" width="600" height="560" fill="url(#room-b)"/>
        </g>
        <path d="M0,222 Q300,300 600,222 L600,252 Q300,332 0,252 Z" fill="url(#silver-b)"/>
        <path d="M0,250 Q300,330 600,250 L600,700 Q300,600 0,700 Z" fill="url(#band-b)"/>
        <path d="M0,700 Q300,600 600,700 L600,732 Q300,640 0,732 Z" fill="url(#silver-b)"/>
        <rect y="1146" width="475" height="54" fill="var(--brand-blue)"/>
        <rect x="475" y="1146" width="125" height="54" fill="var(--sky-blue)"/>
      </g>
    </svg>
    <div class="label__layer brand"><span class="brand__dot"></span><span class="brand__name">Voralux</span></div>
    <h2 class="label__layer title"><span class="title__line title__line--top">SANITARY</span><span class="title__line title__line--bottom">CLEANER</span></h2>
    <p class="label__layer claim"><span class="claim__main">CLEANS, DESCALES &amp; FRESHENS</span><span class="claim__sub">IDEAL FOR QUICK AND POWERFUL CLEANING</span></p>
    <ul class="label__layer usps">
      <li class="usp"><svg class="usp__tick" viewBox="0 0 20 20"><circle cx="10" cy="10" r="8.5" fill="none" stroke="var(--sky-blue)" stroke-width="1.6"/><path d="M6 10.5l3 3 5-7" fill="none" stroke="var(--sky-blue)" stroke-width="1.8"/></svg>Sanitary</li>
      <li class="usp"><svg class="usp__tick" viewBox="0 0 20 20"><circle cx="10" cy="10" r="8.5" fill="none" stroke="var(--sky-blue)" stroke-width="1.6"/><path d="M6 10.5l3 3 5-7" fill="none" stroke="var(--sky-blue)" stroke-width="1.8"/></svg>Bathroom</li>
      <li class="usp"><svg class="usp__tick" viewBox="0 0 20 20"><circle cx="10" cy="10" r="8.5" fill="none" stroke="var(--sky-blue)" stroke-width="1.6"/><path d="M6 10.5l3 3 5-7" fill="none" stroke="var(--sky-blue)" stroke-width="1.8"/></svg>Toilet</li>
      <li class="usp"><svg class="usp__tick" viewBox="0 0 20 20"><circle cx="10" cy="10" r="8.5" fill="none" stroke="var(--sky-blue)" stroke-width="1.6"/><path d="M6 10.5l3 3 5-7" fill="none" stroke="var(--sky-blue)" stroke-width="1.8"/></svg>Wet areas</li>
    </ul>
    <div class="label__layer footer"><span class="footer__note">A READY-TO-USE PRODUCT<br>FOR EVERYDAY USE</span><span class="footer__volume">1000ml</span></div>
  </section>

</main>
</body>
</html>
```